Quillaro Business Cards

Will need a front and back design for a business card for Quillaro.
Can accept the final product as an illustrator file.
www.quillaro.com is the company website.

Target Market(s)

he target market are Chief Technology Officers and people in the tech field.

Industry/Entity Type

Business

Requirements
Must have
• - The business card must have on one of the sides
name
title
company
phone
email
website
The other side may be of some design, derivation of logo and or colors

```html
<!DOCTYPE html>
<html lang="en">
<head>
<meta charset="utf-8">
<title>Quillaro Business Cards</title>
<link href="https://fonts.googleapis.com/css2?family=Arimo:wght@400;700&display=swap" rel="stylesheet">
<style>
  :root {
    --bg: #e9eaec;
    --card-light: #f4f4f5;
    --card-mid: #dcdde0;
    --navy: #1c2f7d;
    --blue: #1f4fb3;
    --blue-deep: #142a78;
    --accent: #2f63c6;
    --steel: #9aa0a8;
    --white: #ffffff;
  }
  * { box-sizing: border-box; margin: 0; padding: 0; }
  html, body { width: 1200px; height: 900px; overflow: hidden; }
  body {
    background: var(--bg);
    font-family: "Arimo", Arial, sans-serif;
    display: flex;
    flex-direction: column;
    align-items: center;
    justify-content: center;
    gap: 60px;
  }
  .card {
    position: relative;
    width: 620px;
    height: 354px;
    border-radius: 22px;
    overflow: hidden;
    box-shadow: 0 6px 18px rgba(0,0,0,.18);
  }
  /* Front */
  .card-front .texture {
    position: absolute; inset: 0;
    background: radial-gradient(ellipse at 40% 30%, var(--card-light) 0%, var(--card-mid) 100%);
  }
  .brand {
    position: absolute;
    display: flex;
    align-items: center;
    gap: 14px;
    white-space: nowrap;
  }
  .brand-dot {
    border-radius: 50%;
    background: var(--navy);
    flex: none;
  }
  .brand-name {
    font-weight: 700;
    color: var(--navy);
    letter-spacing: 0.04em;
    line-height: 1;
  }
  .brand-tagline {
    font-size: 11px;
    letter-spacing: 0.2em;
    color: var(--steel);
    text-transform: uppercase;
    margin-top: 6px;
    white-space: nowrap;
  }
  .brand-web {
    font-size: 12px;
    letter-spacing: 0.14em;
    color: var(--navy);
    margin-top: 10px;
    font-weight: 700;
  }
  .card-front .brand { left: 50%; top: 50%; transform: translate(-50%, -50%); }
  .card-front .brand-dot { width: 92px; height: 92px; }
  .card-front .brand-name { font-size: 44px; }

  /* Back */
  .card-back .panel { position: absolute; inset: 0; }
  .card-back .brand { left: 34px; bottom: 34px; }
  .card-back .brand-dot { width: 58px; height: 58px; }
  .card-back .brand-name { font-size: 28px; }
  .card-back .brand-tagline { font-size: 9px; }
  .info { position: absolute; color: var(--white); white-space: nowrap; }
  .person { left: 34px; top: 32px; }
  .person-name { font-size: 20px; }
  .person-title { font-size: 12px; margin-top: 3px; }
  .company { left: 250px; top: 32px; }
  .company-name { font-size: 18px; font-weight: 700; }
  .company-line { font-size: 12px; margin-top: 3px; }
  .address { margin-top: 12px; font-size: 13px; font-weight: 700; line-height: 1.35; }
  .contacts { left: 430px; top: 130px; list-style: none; font-size: 13px; font-weight: 700; }
  .contacts li { display: flex; align-items: center; gap: 9px; margin-bottom: 10px; }
  .contacts svg { width: 14px; height: 14px; flex: none; }
</style>
</head>
<body>

<section class="card card-front" aria-label="Card front">
  <div class="texture" role="img" aria-label="Soft grey hexagon texture"></div>
  <div class="brand">
    <span class="brand-dot"></span>
    <div>
      <div class="brand-name">Quillaro</div>
      <div class="brand-tagline">Guarding Your Business</div>
      <div class="brand-web">www.quillaro.com</div>
    </div>
  </div>
</section>

<section class="card card-back" aria-label="Card back">
  <svg class="panel" viewBox="0 0 620 354" preserveAspectRatio="none">
    <defs>
      <linearGradient id="blueFill" x1="0" y1="0" x2="1" y2="1">
        <stop offset="0" stop-color="#2458c0"/>
        <stop offset="1" stop-color="#142a78"/>
      </linearGradient>
      <linearGradient id="lightFill" x1="0" y1="0" x2="1" y2="1">
        <stop offset="0" stop-color="#f4f4f5"/>
        <stop offset="1" stop-color="#dcdde0"/>
      </linearGradient>
    </defs>
    <rect width="620" height="354" fill="url(#blueFill)"/>
    <path d="M0 150 C 200 150, 380 230, 470 354 L 0 354 Z" fill="#6f93d8"/>
    <path d="M0 160 C 195 162, 370 240, 452 354 L 0 354 Z" fill="url(#lightFill)"/>
  </svg>

  <div class="info person">
    <div class="person-name">Dana Whitfield</div>
    <div class="person-title">Manager</div>
  </div>

  <div class="info company">
    <div class="company-name">Quillaro</div>
    <div class="company-line">Guarding Your Business</div>
    <div class="address">218 Harbor Lane<br>Easton NY 10230</div>
  </div>

  <ul class="info contacts">
    <li>
      <svg viewBox="0 0 24 24" fill="#fff"><path d="M6.6 10.8a15 15 0 0 0 6.6 6.6l2.2-2.2a1 1 0 0 1 1-.25 11.4 11.4 0 0 0 3.6.57 1 1 0 0 1 1 1V20a1 1 0 0 1-1 1A17 17 0 0 1 3 4a1 1 0 0 1 1-1h3.5a1 1 0 0 1 1 1c0 1.250.2 2.450.57 3.57a1 1 0 0 1-.25 1z"/></svg>
      (555) 204-7731
    </li>
    <li>
      <svg viewBox="0 0 24 24" fill="none" stroke="#fff" stroke-width="2"><rect x="3" y="5" width="18" height="14" rx="1"/><path d="M3 6l9 7 9-7"/></svg>
      info@quillaro.com
    </li>
    <li>
      <svg viewBox="0 0 24 24" fill="none" stroke="#fff" stroke-width="2"><circle cx="12" cy="12" r="9"/><path d="M3 12h18M12 3c3 3 3 15 0 18M12 3c-3 3-3 15 0 18"/></svg>
      www.quillaro.com
    </li>
  </ul>

  <div class="brand">
    <span class="brand-dot"></span>
    <div>
      <div class="brand-name">Quillaro</div>
      <div class="brand-tagline">Guarding Your Business</div>
    </div>
  </div>
</section>

</body>
</html>
```